We need a business card design for a Dubai based company .

We need a business card for a Dubai based company called "Marwaneq Smoking Requisites Trading LLC". We mainly import Flavoured Tobacco products and Charcoal which is used for smoking in a Hookah/Shisha and distribute to the wholesalers and retailers. Logo file is attached herewith.

```html
<!DOCTYPE html>
<html lang="en">
<head>
<meta charset="utf-8">
<title>Marwaneq Smoking Requisites Trading LLC — Business Card</title>
<link rel="stylesheet" href="https://fonts.googleapis.com/css2?family=Arimo:wght@400;700&display=swap">
<style>
  :root {
    --bg-top: #f2f2f0;
    --bg-bottom: #d6d6d4;
    --card: #3a3a3c;
    --card-back: #363638;
    --red: #c1272d;
    --white: #ffffff;
    --rule: #bdbdbd;
    --deboss: #5a5a5d;
  }
  * { margin: 0; padding: 0; box-sizing: border-box; }
  html, body { width: 1200px; height: 801px; overflow: hidden; }
  body {
    background: linear-gradient(180deg, var(--bg-top), var(--bg-bottom));
    font-family: "Arimo", Arial, sans-serif;
    position: relative;
  }
  .card {
    position: absolute;
    top: 246px;
    width: 540px;
    height: 309px;
    background: var(--card);
    box-shadow: 0 10px 24px rgba(0,0,0,0.25);
  }
  .card--front { left: 40px; }
  .card--back { left: 620px; background: var(--card-back); }

  .company-name {
    position: absolute;
    font-weight: 400;
    line-height: 1.2;
  }
  .card--front .company-name {
    right: 36px;
    top: 44px;
    width: 250px;
    text-align: right;
    font-size: 17px;
    color: var(--white);
  }
  .card--back .company-name {
    left: 50%;
    top: 50%;
    transform: translate(-50%, -50%);
    width: 360px;
    text-align: center;
    font-size: 24px;
    color: var(--deboss);
  }

  .holder { position: absolute; left: 36px; top: 104px; }
  .holder__name { color: var(--red); font-weight: 700; font-size: 20px; letter-spacing: 0.5px; }
  .holder__role { color: var(--white); font-size: 17px; margin-top: 2px; }

  .rule {
    position: absolute;
    left: 36px; right: 36px; top: 160px;
    height: 1px;
    background: var(--rule);
  }

  .contacts { position: absolute; left: 36px; top: 176px; list-style: none; }
  .contacts li {
    display: flex; align-items: center; gap: 12px;
    color: var(--white); font-size: 17px;
    height: 26px;
  }
  .contacts svg { width: 15px; height: 15px; flex: none; }

  .address {
    position: absolute; right: 36px; top: 180px;
    color: var(--white); font-size: 17px; line-height: 1.3; text-align: right;
  }
</style>
</head>
<body>
  <section class="card card--front">
    <p class="company-name">Marwaneq Smoking Requisites Trading LLC</p>

    <div class="holder">
      <p class="holder__name">DANIEL REYES</p>
      <p class="holder__role">Manager</p>
    </div>

    <div class="rule"></div>

    <ul class="contacts">
      <li>
        <svg viewBox="0 0 16 16" aria-hidden="true"><path fill="var(--red)" d="M3.5 1.5l2.5 0 1 3.5-1.6 1.2a8 8 0 0 0 4.4 4.4L11 9l3.5 1v2.5c0 1-1 2-2 2A11 11 0 0 1 1.5 3.5c0-1 1-2 2-2z"/></svg>
        <span>123-456-2100</span>
      </li>
      <li>
        <svg viewBox="0 0 16 16" aria-hidden="true"><rect x="1" y="3" width="14" height="10" fill="var(--red)"/><path d="M1 3l7 5.5L15 3" fill="none" stroke="var(--card)" stroke-width="1.3"/></svg>
        <span>youremail@mailbox.com</span>
      </li>
      <li>
        <svg viewBox="0 0 16 16" aria-hidden="true"><circle cx="8" cy="8" r="7" fill="var(--red)"/><g fill="none" stroke="var(--card)" stroke-width="1"><ellipse cx="8" cy="8" rx="3" ry="7"/><path d="M1 8h14M2.5 4.5h11M2.5 11.5h11"/></g></svg>
        <span>www.yourwebsite.com</span>
      </li>
    </ul>

    <p class="address">Your address, city<br>state, ZIP 0000</p>
  </section>

  <section class="card card--back">
    <p class="company-name">Marwaneq Smoking Requisites Trading LLC</p>
  </section>
</body>
</html>
```